Kindle Book Cover for Teen Financial Niche

Had a temporary cover done for the book but it needs a lot better cover now it is starting to get some traction.
The current book can be seen here:
https://www.bookvalemart.com/dp/Q7K42LZ9RT
I am wanting something very different if possible. Please search books in the teen financial niche on Bookvale and you will see that a lot of the covers are very similar in style.
I am looking for something different that will stand out in a crowded marketplace.
If you are putting someone on the cover please use a male character rather than a female one.
Thanks
Dale

```html
<!DOCTYPE html>
<html lang="en">
<head>
<meta charset="UTF-8">
<title>Everyday Cashflow – Cash Control</title>
<link href="https://fonts.googleapis.com/css2?family=Anton&family=Open+Sans:ital,wght@0,400;0,700;0,800;1,400&family=Roboto+Condensed:wght@400;700;800&display=swap" rel="stylesheet">
<style>
  :root {
    --denim-deep: #0b1a33;
    --denim-mid: #1b3461;
    --denim-light: #2a4a7f;
    --bill-cream: #dcd9c8;
    --bill-shade: #8f8f84;
    --title-white: #f1f1ee;
    --gold-dark: #a97d1c;
    --gold-mid: #d8ab38;
    --gold-light: #f3d872;
    --ink: #0a1226;
    --label-white: #ffffff;
  }
  * { margin: 0; padding: 0; box-sizing: border-box; }
  html, body {
    width: 676px; height: 1200px; overflow: hidden;
    background: var(--denim-deep);
  }
  .cover {
    position: relative;
    width: 676px; height: 1200px;
    overflow: hidden;
    font-family: "Open Sans", sans-serif;
    color: var(--label-white);
  }
  .cover-photo {
    position: absolute; inset: 0;
    background:
      radial-gradient(ellipse 48% 17% at 55% 22%, var(--bill-cream) 0%, var(--bill-shade) 60%, transparent 100%),
      radial-gradient(ellipse 80% 50% at 50% 60%, var(--denim-mid) 0%, var(--denim-deep) 100%),
      linear-gradient(180deg, var(--denim-light) 0%, var(--denim-deep) 100%);
  }
  .title {
    position: absolute; left: 0; right: 0;
    display: block;
    text-align: center;
    font-family: "Anton", sans-serif;
    font-weight: 400;
    line-height: 1;
    white-space: nowrap;
  }
  .title-main {
    top: 442px;
    font-size: 146px;
    letter-spacing: 1px;
    color: var(--title-white);
  }
  .title-accent {
    top: 588px;
    font-size: 146px;
    letter-spacing: 4px;
    background: linear-gradient(90deg, var(--gold-dark) 0%, var(--gold-mid) 45%, var(--gold-light) 100%);
    -webkit-background-clip: text; background-clip: text;
    color: transparent;
  }
  .tagline-label {
    position: absolute; left: 50%; top: 744px;
    transform: translateX(-50%) rotate(-4deg);
    background: var(--label-white);
    color: var(--ink);
    font-weight: 800;
    font-size: 30px;
    line-height: 1.2;
    padding: 6px 14px;
    border-radius: 6px;
    white-space: nowrap;
  }
  .subtitle {
    position: absolute; left: 60px; right: 60px; top: 830px;
    text-align: center;
    font-size: 22px; line-height: 1.3;
    color: var(--label-white);
  }
  .subtitle em { font-style: italic; }
  .audience {
    position: absolute; left: 0; right: 0; top: 1040px;
    text-align: center;
    font-family: "Roboto Condensed", sans-serif;
    font-size: 30px;
    line-height: 1.1;
    color: var(--label-white);
  }
  .author-band {
    position: absolute; left: 0; right: 0; bottom: 0; height: 110px;
    background: linear-gradient(90deg, var(--gold-dark) 0%, var(--gold-mid) 50%, var(--gold-light) 100%);
    display: flex; align-items: center; justify-content: center;
  }
  .author-name {
    font-family: "Roboto Condensed", sans-serif;
    font-weight: 800;
    font-size: 80px;
    color: var(--ink);
    line-height: 1;
  }
</style>
</head>
<body>
  <main class="cover">
    <div class="cover-photo" role="img" aria-label="Dark blue denim jeans back pocket with a fan of banknotes tucked in the top"></div>
    <h1>
      <span class="title title-main">EVERYDAY</span>
      <span class="title title-accent">CASHFLOW</span>
    </h1>
    <p class="tagline-label">CASH CONTROL</p>
    <p class="subtitle"><em>A Field Guide to</em> Income, Budgets, Smart Spending, Saving and Growing Wealth</p>
    <p class="audience">FOR TEENS AND YOUNG ADULTS</p>
    <div class="author-band">
      <p class="author-name">LIAM CASTELL</p>
    </div>
  </main>
</body>
</html>
```